Lumen Harbor Business Card Design Project

We have recently rebranded and would like to design new business cards that incorporate the corporate logo - double sided cards with corporate logo on one side and contact details on the other

Target Market(s)

Sophisticated and high net worth investors and finance industry professionals

Industry/Entity Type

Funds Management

Contact Information for Business Card

The card should prominently feature the company name and logo. Other details will be standard contact details for each staff member - name, address, phone, email, website

Colors
0054AA
0677BA
7BADD7
CADEEF
E8F1F8

Requirements
Must have
• Double-sided design with one side prominently featuring the corporate logo and the other side with all standard contact details

```html
<!DOCTYPE html>
<html lang="en">
<head>
<meta charset="utf-8">
<title>Lumen Harbor Business Card</title>
<link href="https://fonts.googleapis.com/css2?family=Jost:wght@400;500&family=Open+Sans:wght@400&display=swap" rel="stylesheet">
<style>
  :root {
    --stage: #ababab;
    --navy: #1f4574;
    --sail: #2a63a1;
    --sail-light: #7badd7;
    --paper: #ffffff;
    --ink-grey: #6b6b6b;
    --rule: #8a9bb3;
  }
  html, body {
    margin: 0;
    width: 1200px;
    height: 1000px;
    overflow: hidden;
    background: var(--stage);
  }
  .canvas {
    position: relative;
    width: 1200px;
    height: 1000px;
  }
  .card {
    position: absolute;
    top: 338px;
    width: 514px;
    height: 297px;
    overflow: hidden;
  }
  .card--back {
    left: 57px;
    background: var(--navy);
    display: flex;
    align-items: center;
    justify-content: center;
  }
  .card--back .wordmark {
    position: static;
    gap: 16px;
  }
  .card--back .wordmark__square {
    width: 26px;
    height: 26px;
    background: var(--sail-light);
  }
  .card--back .wordmark__name {
    font-size: 42px;
    color: var(--sail-light);
  }
  .card--front {
    left: 614px;
    background: var(--paper);
    font-family: "Open Sans", sans-serif;
  }
  .wordmark {
    position: absolute;
    top: 54px;
    left: 0;
    right: 0;
    display: flex;
    justify-content: center;
    align-items: center;
    gap: 14px;
  }
  .wordmark__square {
    width: 22px;
    height: 22px;
    background: var(--navy);
  }
  .wordmark__name {
    font-family: "Jost", sans-serif;
    font-weight: 500;
    font-size: 36px;
    letter-spacing: 1.5px;
    text-transform: uppercase;
    color: var(--navy);
    line-height: 1;
  }
  .person {
    position: absolute;
    top: 155px;
    right: 289px;
    text-align: right;
    font-family: "Jost", sans-serif;
    color: var(--navy);
  }
  .person__name {
    font-size: 19px;
    font-weight: 500;
    letter-spacing: 1.6px;
    text-transform: uppercase;
    line-height: 1;
  }
  .person__title {
    margin-top: 6px;
    font-size: 10px;
    letter-spacing: 1.2px;
    text-transform: uppercase;
    color: var(--ink-grey);
    line-height: 1;
  }
  .divider {
    position: absolute;
    left: 237px;
    top: 149px;
    width: 1.5px;
    height: 46px;
    background: var(--rule);
  }
  .contact {
    position: absolute;
    left: 250px;
    top: 145px;
    margin: 0;
    padding: 0;
    list-style: none;
    font-size: 14px;
    line-height: 17px;
    color: var(--ink-grey);
  }
  .address {
    position: absolute;
    left: 0;
    right: 0;
    top: 257px;
    margin: 0;
    text-align: center;
    font-size: 14px;
    line-height: 20px;
    color: var(--ink-grey);
  }
</style>
</head>
<body>
<main class="canvas">
  <section class="card card--back">
    <div class="wordmark">
      <span class="wordmark__square"></span>
      <span class="wordmark__name">Lumen Harbor</span>
    </div>
  </section>

  <section class="card card--front">
    <div class="wordmark">
      <span class="wordmark__square"></span>
      <span class="wordmark__name">Lumen Harbor</span>
    </div>
    <div class="person">
      <div class="person__name">Daniel Whitcombe</div>
      <div class="person__title">Portfolio Manager</div>
    </div>
    <span class="divider"></span>
    <ul class="contact">
      <li>+02 9000 4173</li>
      <li>portfolio@lumenharbor.com</li>
      <li>www.lumenharbor.com</li>
    </ul>
    <p class="address">Level 14 Quayside Tower, 21 Harbour Lane, Sydney NSW 2000</p>
  </section>
</main>
</body>
</html>
```